Dental Business Card Design w/logo

Classic, elegant w/a touch of contemporary
Upscale dental facility located in Modesto CA
Specializing in restorative & general dentistry
Providing exceptional customer service to the community
Updates

I prefer script and not bold writing
If you can use the phone; fax and email icons instead of spelling them out, it would be great
No bold colors
Classy and elegant
In the back of the card I would like to see something like this
Your Next Appointment:
Mon     Tue    Wed    Thur (a box next to each of them for marking)
Date:_______________ at_____________ AM    PM  (a box next to them for marking)

Thank you

Target Market(s)

Well established professional

Industry/Entity Type

Dental

Contact Information for Business Card

Lavinteya Morbundi DMD
4176 Larkspur Rd
Suite F7
Modesto, CA 95355

Office: 209-731-5902
Fax: 209-731-8417
Email: morbundidmd@velmoranet.com

Requirements
Must have
• Unique classic logo
An easily repeatable design that can be used on letterhead and envelopes
Nice to have
• My initials incorporated into unique design
Should not have
• No cartoons or cheesy themes. This is a practice for the well established and professional individual.

```html
<!DOCTYPE html>
<html lang="en">
<head>
<meta charset="utf-8">
<title>Morbundi Dental – Business Card</title>
<link href="https://fonts.googleapis.com/css2?family=Great+Vibes&family=Dancing+Script:wght@400&display=swap" rel="stylesheet">
<style>
  :root{
    --page:#ecebe8;
    --card:#d6c49a;
    --band-brown:#603913;
    --band-dark:#1f150c;
    --ink:#1c1510;
    --cream:#f3ead8;
    --icon:#b5651d;
    --disc:#f1f1ef;
  }
  *{margin:0;padding:0;box-sizing:border-box}
  html,body{width:1200px;height:1200px;overflow:hidden;background:var(--page)}
  .sheet{position:relative;width:1200px;height:1200px}
  .card{position:absolute;left:190px;width:820px;height:470px;background:var(--card);
        box-shadow:0 6px 18px rgba(0,0,0,.18);overflow:hidden;color:var(--ink)}
  .card--back{top:80px}
  .card--front{top:650px}
  .band-left{position:absolute;left:0;top:0;width:170px;height:100%;background:var(--band-brown)}
  .band-right{position:absolute;right:0;top:0;width:110px;height:100%;background:var(--band-dark)}
  .brand-mark{position:absolute;left:0;top:50px;width:170px;text-align:center;
              font-family:"Great Vibes",cursive;font-size:34px;line-height:1.1;color:var(--cream)}
  .brand-disc{position:absolute;left:15px;top:100px;width:80px;height:80px;border-radius:50%;background:var(--disc)}
  .brand-side{position:absolute;left:0;top:195px;width:110px;text-align:center;
              font-family:"Great Vibes",cursive;font-size:24px;line-height:1.15;color:var(--cream)}
  .name{position:absolute;left:225px;top:95px;font-family:"Great Vibes",cursive;font-size:50px;white-space:nowrap}
  .name small{font-family:"Dancing Script",cursive;font-size:28px;margin-left:10px}
  .address{position:absolute;left:290px;top:172px;font-family:"Dancing Script",cursive;font-size:28px;line-height:1.2}
  .contacts{position:absolute;left:210px;top:290px;list-style:none;font-family:"Dancing Script",cursive;font-size:29px;line-height:1.35}
  .contacts li{display:flex;align-items:center;gap:12px}
  .contacts svg{width:28px;height:28px;flex:none}
  .appt-title{position:absolute;left:220px;top:70px;font-family:"Great Vibes",cursive;font-size:50px;white-space:nowrap}
  .appt-row{position:absolute;left:220px;display:flex;align-items:center;gap:14px;
            font-family:"Great Vibes",cursive;font-size:42px;white-space:nowrap}
  .appt-row--days{top:190px}
  .appt-row--time{top:300px}
  .tick-box{display:inline-block;width:30px;height:38px;border:2px solid var(--ink);background:#fff;margin-right:16px}
  .blank{display:inline-block;border-bottom:2px solid var(--ink);height:30px}
</style>
</head>
<body>
<main class="sheet">

  <section class="card card--back" aria-label="Appointment card reverse">
    <div class="band-left"><div class="brand-mark">Morbundi<br>Dental</div></div>
    <p class="appt-title">Your Next Appointment:</p>
    <p class="appt-row appt-row--days">
      Mon <span class="tick-box"></span> Tue <span class="tick-box"></span>
      Wed <span class="tick-box"></span> Thur <span class="tick-box"></span>
    </p>
    <p class="appt-row appt-row--time">
      Date: <span class="blank" style="width:140px"></span> at <span class="blank" style="width:90px"></span>
      a.m. <span class="tick-box"></span> p.m. <span class="tick-box"></span>
    </p>
  </section>

  <section class="card card--front" aria-label="Business card front">
    <div class="band-left"><div class="brand-mark">Morbundi<br>Dental</div></div>
    <p class="name">Lavinteya Morbundi<small>DMD</small></p>
    <p class="address">4176 Larkspur Rd, Suite F7<br>Modesto, CA 95355</p>
    <ul class="contacts">
      <li>
        <svg viewBox="0 0 28 28" aria-label="Office phone"><path fill="var(--icon)" d="M4 10c0-4 20-4 20 0v3h-5v-3H9v3H4z"/><rect x="6" y="14" width="16" height="10" rx="2" fill="var(--icon)"/><circle cx="14" cy="19" r="3" fill="var(--card)"/></svg>
        209.731.5902
      </li>
      <li>
        <svg viewBox="0 0 28 28" aria-label="Fax"><rect x="8" y="3" width="12" height="8" fill="none" stroke="var(--icon)" stroke-width="2"/><rect x="3" y="11" width="22" height="10" rx="2" fill="var(--icon)"/><rect x="8" y="18" width="12" height="7" fill="var(--card)" stroke="var(--icon)" stroke-width="2"/></svg>
        209.731.8417
      </li>
      <li>
        <svg viewBox="0 0 28 28" aria-label="Email"><path d="M3 12 14 4l11 8v12H3z" fill="none" stroke="var(--icon)" stroke-width="2"/><path d="M3 12l11 8 11-8" fill="none" stroke="var(--icon)" stroke-width="2"/></svg>
        morbundidmd@velmoranet.com
      </li>
    </ul>
    <div class="band-right">
      <div class="brand-disc"></div>
      <div class="brand-side">Morbundi<br>Dental</div>
    </div>
  </section>

</main>
</body>
</html>
```